Design a 4 Page Brochure

The objective is very simple.

You need to design a 4 page brochure for a product of a company. First page would of-course be the title / cover page setting the overall theme, 2nd will have text content within the same theme with relevant graphics etc, covering one part of the overall product. 3rd page will be similar to the second one with difference in content and relevant graphics. 4th is the last page and actually the back page having address, contact information, logos etc.

Selection of theme and Graphics must be according to the name of the product.

It is suggested to read the "Guidelines" file and the other 2 "Content Files" before you start as it will help you with the task in details and also identify what kind of graphics you should be using in order to elaborate the content aesthetically and purposefully.

I will posting more similar contests so the winner could continuously benefit. Show some genuine creativity.

```html
<!DOCTYPE html>
<html lang="en">
<head>
<meta charset="utf-8">
<title>Keystone Brochure Spread</title>
<link rel="stylesheet" href="https://fonts.googleapis.com/css2?family=Lora:wght@400;700&family=Open+Sans:wght@400;600;700&display=swap">
<style>
:root{
  --charcoal:#4a4a4c;
  --orange:#f6a51d;
  --paper:#ffffff;
  --gutter:#ececec;
  --ink:#555558;
  --ink-soft:#7a7a7d;
}
*{box-sizing:border-box;margin:0;padding:0}
html,body{width:1200px;height:413px;overflow:hidden;background:#fff}
body{font-family:"Open Sans",Arial,sans-serif;color:var(--ink)}
.spread{position:relative;width:1200px;height:413px;overflow:hidden}
.page{position:absolute;top:0;height:413px;overflow:hidden}
p,li{font-size:4.6px;line-height:1.45}
ul{list-style:none}
li{position:relative;padding-left:6px}
li::before{content:"";position:absolute;left:0;top:2px;width:2.4px;height:2.4px;border-radius:50%;background:var(--orange)}

/* cover */
.cover{left:0;width:205px;background:var(--charcoal)}
.cover .shade{position:absolute;inset:0}
.cover .brand{position:absolute;left:95px;top:206px;font-family:"Lora",Georgia,serif;font-size:13px;letter-spacing:1px;color:var(--orange)}
.cover .tagline{position:absolute;left:96px;top:224px;font-size:4.4px;letter-spacing:1.2px;color:#d8d8d8}

/* shared parts */
.masthead{position:absolute;top:0;height:40px;background:var(--charcoal)}
.masthead h1{position:absolute;top:13px;font-family:"Lora",Georgia,serif;font-weight:400;font-size:11px;color:var(--orange)}
.tab{position:absolute;background:var(--orange)}
.band{position:absolute;background:var(--charcoal)}
.block{position:absolute}
.label{font-family:"Lora",Georgia,serif;font-size:7px;font-weight:700;color:var(--orange);letter-spacing:.4px;text-transform:uppercase}
.bar-label{position:absolute;height:13px;background:var(--charcoal);color:var(--orange);font-family:"Lora",Georgia,serif;font-size:6.4px;font-weight:700;padding:3px 0 0 10px;letter-spacing:.4px;text-transform:uppercase}
.bar-label::before{content:"";position:absolute;left:0;top:0;width:5px;height:13px;background:var(--orange)}
.icon-row{position:absolute;display:flex;gap:8px}
.icon-row .item{width:58px}
.icon-row svg{display:block;margin-bottom:3px}
.sub{font-size:6px;font-weight:700;color:var(--charcoal)}
.quote{position:absolute;border:0.8px solid #bdbdbd;padding:4px 5px;background:#fff}
.cols{position:absolute;display:flex;gap:5px}
.cols p{width:60px}

/* page 2 */
.assess{left:205px;width:235px;background:var(--paper)}
/* page 3 */
.train{left:440px;width:240px;background:var(--paper)}
/* page 4 */
.back{left:680px;width:520px;background:var(--paper)}
.back .head{position:absolute;left:22px;font-family:"Lora",Georgia,serif;font-size:6.6px;font-weight:700;color:var(--orange);letter-spacing:.3px;text-transform:uppercase;padding-left:8px}
.back .head::before{content:"";position:absolute;left:0;top:0;width:4px;height:9px;background:var(--charcoal)}
.partners{position:absolute;left:330px;top:318px;width:120px}
.partners .intro{font-size:4.4px;color:var(--ink-soft);margin-bottom:3px;font-style:italic}
.partner{display:flex;align-items:center;gap:3px;margin-bottom:4px;font-weight:700;font-size:9px;color:var(--charcoal)}
.partner .dot{width:7px;height:7px;border-radius:50%;background:var(--orange)}
.partner .sq{width:7px;height:7px;background:var(--charcoal)}
.contact{position:absolute;left:378px;top:370px;width:88px}
.contact p{font-size:4.2px;color:var(--ink-soft)}
</style>
</head>
<body>
<div class="spread">

  <!-- Cover -->
  <section class="page cover">
    <svg class="shade" width="205" height="413" viewBox="0 0 205 413">
      <polygon points="0,0 150,0 120,170 0,200" fill="#444446"/>
      <polygon points="120,170 205,160 205,413 60,413" fill="#535355"/>
      <rect x="190" y="0" width="10" height="70" fill="var(--orange)"/>
      <rect x="180" y="20" width="6" height="40" fill="var(--orange)"/>
      <rect x="190" y="300" width="10" height="113" fill="var(--orange)"/>
      <rect x="180" y="330" width="6" height="60" fill="var(--orange)"/>
    </svg>
    <div class="brand">KEYSTONE</div>
    <div class="tagline">ASSESS | TRAIN | GROW</div>
  </section>

  <!-- Page 2 -->
  <section class="page assess">
    <div class="masthead" style="left:0;width:235px"><h1 style="left:40px">Why Assess Talent?</h1></div>
    <div class="tab" style="left:10px;top:0;width:12px;height:56px"></div>
    <p class="block" style="left:28px;top:46px;width:190px">In today's competitive environment an organization has to be able to drive profitable growth through their biggest asset, their people. More than ever, businesses are under increasing pressure not only to recruit but retain and develop the best people. Critical areas for organizations include:</p>
    <div class="icon-row" style="left:28px;top:82px">
      <div class="item">
        <svg width="24" height="14" viewBox="0 0 24 14"><circle cx="5" cy="4" r="2.5" fill="var(--charcoal)"/><circle cx="12" cy="4" r="2.5" fill="var(--orange)"/><circle cx="19" cy="4" r="2.5" fill="var(--charcoal)"/><rect x="2" y="8" width="6" height="6" rx="2" fill="var(--charcoal)"/><rect x="9" y="8" width="6" height="6" rx="2" fill="var(--orange)"/><rect x="16" y="8" width="6" height="6" rx="2" fill="var(--charcoal)"/></svg>
        <p>Identify high performers and successors to key positions</p>
      </div>
      <div class="item">
        <svg width="24" height="14" viewBox="0 0 24 14"><circle cx="12" cy="4" r="3" fill="var(--orange)"/><rect x="8" y="8" width="8" height="6" rx="2" fill="var(--orange)"/><circle cx="4" cy="7" r="2" fill="var(--charcoal)"/><circle cx="20" cy="7" r="2" fill="var(--charcoal)"/></svg>
        <p>Develop Managers and Leaders to reinforce culture, instill values, and create a sustainable "leadership pipeline"</p>
      </div>
      <div class="item">
        <svg width="24" height="14" viewBox="0 0 24 14"><rect x="2" y="8" width="4" height="6" fill="var(--charcoal)"/><rect x="8" y="5" width="4" height="9" fill="var(--orange)"/><rect x="14" y="2" width="4" height="12" fill="var(--charcoal)"/><path d="M19 3 l3 0 l0 3" stroke="var(--orange)" fill="none" stroke-width="1"/></svg>
        <p>How do we quickly identify competency gaps so we can deliver training or development programs to fill these gaps?</p>
      </div>
    </div>
    <div class="block label" style="left:28px;top:135px">Our Solutions</div>
    <p class="block" style="left:28px;top:146px;width:190px">We provide a range of assessment services including Assessment Centres &amp; multitude of Psychometric Testing.</p>
    <svg class="block" style="left:28px;top:164px" width="14" height="14" viewBox="0 0 14 14"><circle cx="7" cy="7" r="7" fill="var(--orange)"/><circle cx="7" cy="5" r="2.2" fill="#fff"/><rect x="4" y="8" width="6" height="3.5" rx="1.5" fill="#fff"/></svg>
    <div class="block" style="left:46px;top:163px;width:82px">
      <div class="sub">Personality Tests</div>
      <p>Personality tests help employers at various levels, by unearthing their potential by increasing their level of insight and self-awareness.</p>
    </div>
    <div class="quote" style="left:134px;top:162px;width:84px"><p style="font-style:italic">Successful organizations around the world use Psychometric testing to measure motivation, personalities, intelligence, reasoning.</p></div>
    <svg class="block" style="left:28px;top:206px" width="14" height="14" viewBox="0 0 14 14"><circle cx="7" cy="7" r="7" fill="var(--orange)"/><path d="M4 7 l2 2 l4 -4" stroke="#fff" stroke-width="1.3" fill="none"/></svg>
    <div class="block" style="left:46px;top:205px;width:172px">
      <div class="sub">Assessment &amp; Development centers</div>
      <p>Experts at Norvale use researched activities including in tray exercise, in basket exercises, simulations, role plays, ability tests, behavioral tests and other tools to make sure that a candidate has been evaluated thoroughly.</p>
      <p>An assessment centre employs multiple assessment methods and exercises to evaluate a wide range of competencies used to make a variety of employment decisions including:</p>
      <ul style="margin-top:2px">
        <li>Selecting the best talent</li>
        <li>Promoting the top employees</li>
        <li>Succession planning &amp; development</li>
      </ul>
    </div>
    <div class="bar-label" style="left:28px;top:280px;width:120px">How Can We Help</div>
    <p class="block" style="left:28px;top:299px;width:190px">We provide talent solutions using world top psychometric tools. Our key features include:</p>
    <div class="cols" style="left:28px;top:314px">
      <p>Full range of Psychometric Services by Registered &amp; Qualified Business Psychologists and psychometricians</p>
      <p>Scientific Assessments that help organizations Assess, Select and develop the right people for the right roles</p>
      <p>Assessment &amp; Development Centers and Competency Mapping for Executives and Senior Managers</p>
    </div>
    <div class="tab" style="left:10px;top:370px;width:12px;height:43px"></div>
    <div class="band" style="left:223px;top:0;width:12px;height:413px"></div>
    <div class="tab" style="left:223px;top:60px;width:12px;height:90px"></div>
    <div class="tab" style="left:223px;top:370px;width:12px;height:43px"></div>
  </section>

  <!-- Page 3 -->
  <section class="page train">
    <div class="masthead" style="left:0;width:226px"><h1 style="left:46px">Why Train People?</h1></div>
    <div class="tab" style="left:16px;top:0;width:10px;height:56px"></div>
    <p class="block" style="left:36px;top:46px;width:180px">A business has as its people learn. If your business isn't learning, then you're lagging behind. Employees come, often, protect, defend and manage your products or services every day, year on year. Business leaders of today understand the importance of providing employees with opportunities to learn and grow personally and professionally.</p>
    <div class="bar-label" style="left:36px;top:92px;width:120px">Style and Approach</div>
    <p class="block" style="left:36px;top:110px;width:180px">We are known for our up-beat, energised style of delivery that is motivational, always practical and commercially orientated. Our consultants are selected because they are credible, charismatic, highly qualified and excellent communicators. We can make the driest subject into an engaging and informative learning session that is enjoyable and good fun.</p>
    <div class="bar-label" style="left:36px;top:157px;width:90px">Difference</div>
    <ul class="block" style="left:36px;top:175px;width:180px">
      <li>Our range of courses and learning system can enhance your management and leadership abilities, no matter how much experience you have as a manager.</li>
      <li>Our programs are grounded in a model of transformative learning. Unlike informative learning, the transformational experience has all that it takes for a person to rediscover self and the hidden potential within.</li>
      <li>Design and provide short-term, practical, high quality and commercially focused solutions that consistently exceed the expectations of clients.</li>
      <li>Sustain ourselves as a trustworthy, profitable and professional consultancy solutions provider capable of rapid adaptation to changing needs and conditions.</li>
    </ul>
    <div class="bar-label" style="left:36px;top:262px;width:110px">Training Areas</div>
    <p class="block" style="left:36px;top:280px;width:180px">Our range of management courses and leadership training can be tailored to meet your organizational specific needs. We work with our clients in order to fully understand their needs and to deliver a practical leadership training program that will give incredible results. Our domains include:</p>
    <ul class="block" style="left:36px;top:318px;width:88px">
      <li>Management Trainings</li>
      <li>Interpersonal Development</li>
      <li>Signature Series Workshops</li>
      <li>Leadership &amp; Strategy</li>
    </ul>
    <ul class="block" style="left:128px;top:318px;width:90px">
      <li>Personal Development</li>
      <li>Team Building Programs</li>
      <li>Adventure Learning</li>
      <li>Service &amp; Sales Trainings</li>
    </ul>
    <div class="tab" style="left:16px;top:370px;width:10px;height:43px"></div>
    <div class="block" style="left:226px;top:0;width:14px;height:413px;background:var(--gutter)"></div>
  </section>

  <!-- Back page -->
  <section class="page back">
    <div class="head" style="top:10px">Working Closely With The Clients</div>
    <p class="block" style="left:22px;top:24px;width:300px">Each program is finalized after detailed deliberations with the client organizations and thorough understanding of the background of the participants. We analyze the need of the client to make sure that the training is as relevant to business needs as possible. Our trainings include interactive discussions, role plays, case studies and exercises amongst others which go a long way to facilitate the delegates to appreciate and practice the desired skills.</p>
    <div class="head" style="top:80px">Executive Coaching and Assessment</div>
    <p class="block" style="left:22px;top:94px;width:300px">From High Potential individuals to Senior Leaders and C Level Executives, our executive coaching services are targeted to your needs. Our approach includes multirater assessments, feedback, goal setting, development planning and implementation support. Executive coaching is based on proven growth, insight and reflection models.</p>
    <div class="head" style="top:128px">Post Training Support</div>
    <p class="block" style="left:22px;top:142px;width:300px">For our training sessions we prepare a detailed and thorough delegate folder which includes the key exercises and concepts covered in the session. It helps the participants during the transfer of training once back at work so they can comfortably relate the concepts covered in detail in the session with work.</p>
    <ul class="block" style="left:22px;top:176px;width:300px">
      <li>We can develop a training implementation plan and also arrange post training impact assessment where ever desired by clients.</li>
      <li>Over 70% of our courses are bespoke, designed to meet with a detailed and specific brief from the client.</li>
      <li>Every training is targeted at fulfilling the particular needs of the organization. Our trainers &amp; consultants are internationally accredited &amp; have had decades of industry experience, both domestically and globally, which brings us to the pole position to deliver training &amp; consultancy services in the most effective and efficient manner.</li>
    </ul>
    <div class="partners">
      <div class="intro">A Product of</div>
      <div class="partner"><span class="dot"></span>Norvale Consulting</div>
      <div class="partner"><span class="sq"></span>Brightpath</div>
    </div>
    <div class="contact">
      <p>Address: 48 Harbour Row, Fairhaven</p>
      <p>Phone: +1 555 010 2040</p>
      <p>Fax: +1 555 010 2041</p>
      <p>Email: hello@keystone-example.com</p>
      <p>Web: www.keystone-example.com</p>
    </div>
    <div class="band" style="left:468px;top:0;width:52px;height:413px"></div>
    <div class="tab" style="left:482px;top:0;width:10px;height:70px"></div>
    <div class="tab" style="left:498px;top:20px;width:6px;height:40px"></div>
    <div class="tab" style="left:482px;top:300px;width:10px;height:113px"></div>
  </section>

</div>
</body>
</html>
```